Business card design for a engineering company

I need a double sided business card design for my company "Verdmont Flow Solutions". The card will be used in Malaysia. Sleek and professional, with a little design flare to it.
Information to showcase:
1. Company logo
2. Name, title, phone, email address, website address
3. our products "Pumping technology, Valve & actuation, Air Moving Technology
Example:
Ravi Tanaka
Business manager
ravi.tanaka@verdmont-example.com
www.verdmont-example.com.my
- Pumping technology
- Valve & actuation
- Air moving technology
Target Market(s)
engineers, purchasing managers
Industry/Entity Type
Business
Contact Information for Business Card
Ravi Tanaka
Business manager
ravi.tanaka@verdmont-example.com
www.verdmont-example.com.my
- Pumping technology
- Valve & actuation
- Air moving technology
catch phrase : "Solving flow challenges, exceeding expectations"

```html
<!DOCTYPE html>
<html lang="en">
<head>
<meta charset="utf-8">
<title>Verdmont Flow Solutions – Business Card</title>
<link rel="stylesheet" href="https://fonts.googleapis.com/css2?family=Open+Sans:ital,wght@0,400;0,600;0,700;1,400&display=swap">
<style>
  :root {
    --page-bg: #2a2a2c;
    --card-white: #ffffff;
    --navy: #0e3347;
    --orange-light: #f7a21b;
    --orange-dark: #e8631a;
    --ink: #3b4a55;
    --ink-soft: #5d6a73;
    --on-navy: #ffffff;
  }
  * { box-sizing: border-box; margin: 0; padding: 0; }
  html, body {
    width: 1200px; height: 950px; overflow: hidden;
    background: var(--page-bg);
    font-family: "Open Sans", Arial, sans-serif;
  }
  .sheet {
    width: 1200px; height: 950px;
    display: flex; flex-direction: column; align-items: center; justify-content: center;
    gap: 28px;
  }
  .card {
    position: relative;
    width: 760px; height: 434px;
    overflow: hidden;
  }
  .card-front { background: var(--card-white); color: var(--ink); }
  .card-back { background: var(--navy); color: var(--on-navy); }
  .card-shapes { position: absolute; inset: 0; }

  /* Company name, set as plain text */
  .company-name {
    position: absolute;
    font-weight: 600;
    line-height: 1.2;
    white-space: nowrap;
  }
  .card-front .company-name { left: 250px; top: 140px; font-size: 30px; color: var(--navy); }
  .card-back .company-name { left: 120px; top: 160px; font-size: 36px; color: var(--on-navy); }

  /* Contact block */
  .contact { position: absolute; left: 250px; top: 262px; }
  .contact-name { font-size: 22px; font-weight: 700; text-transform: uppercase; color: var(--ink); letter-spacing: 0.02em; }
  .contact-title { font-size: 18px; color: var(--orange-dark); margin-top: 2px; margin-bottom: 12px; }
  .contact-list { list-style: none; }
  .contact-list li { display: flex; align-items: center; gap: 10px; font-size: 15px; color: var(--ink-soft); line-height: 1.75; }
  .contact-list svg { width: 16px; height: 16px; flex: none; }

  /* Back */
  .tagline { position: absolute; left: 120px; top: 110px; font-size: 17px; font-style: italic; letter-spacing: 0.01em; }
  .products { position: absolute; left: 120px; top: 290px; font-size: 17px; letter-spacing: 0.01em; }
  .products .sep { margin: 0 8px; }
</style>
</head>
<body>
<main class="sheet">

  <section class="card card-front" aria-label="Business card front">
    <svg class="card-shapes" viewBox="0 0 760 434" aria-hidden="true">
      <defs>
        <linearGradient id="orange-fade" x1="0" y1="0" x2="1" y2="1">
          <stop offset="0" stop-color="#f7a21b"/>
          <stop offset="1" stop-color="#e8631a"/>
        </linearGradient>
      </defs>
      <path class="corner-accent" d="M540 0 H760 V220 A220 220 0 0 0 540 0 Z" fill="url(#orange-fade)"/>
      <path class="corner-band" d="M0 200 V434 H234 A234 234 0 0 1 0 200 Z" fill="#0e3347"/>
    </svg>

    <p class="company-name">Verdmont Flow Solutions</p>

    <div class="contact">
      <h1 class="contact-name">Ravi Tanaka</h1>
      <p class="contact-title">Business manager</p>
      <ul class="contact-list">
        <li>
          <svg viewBox="0 0 16 16" aria-hidden="true"><path d="M4 1.5l2.2 3-1.3 1.6a9 9 0 0 0 5 5l1.6-1.3 3 2.2-1.4 2.4C8 14.5 1.5 8 1.6 2.9z" fill="#5d6a73"/></svg>
          601 555 0142
        </li>
        <li>
          <svg viewBox="0 0 16 16" aria-hidden="true"><rect x="1" y="3" width="14" height="10" rx="1.5" fill="#5d6a73"/><path d="M1.8 4l6.2 5 6.2-5" stroke="#fff" stroke-width="1.3" fill="none"/></svg>
          ravi.tanaka@verdmont-example.com
        </li>
        <li>
          <svg viewBox="0 0 16 16" aria-hidden="true"><circle cx="8" cy="8" r="7" fill="#5d6a73"/><path d="M1.5 8h13M8 1c2.6 2.8 2.6 11.2 0 14M8 1c-2.6 2.8-2.6 11.2 0 14" stroke="#fff" stroke-width="1" fill="none"/></svg>
          www.verdmont-example.com.my
        </li>
      </ul>
    </div>
  </section>

  <section class="card card-back" aria-label="Business card back">
    <p class="tagline">Solving flow challenges, exceeding expectations</p>
    <p class="company-name">Verdmont Flow Solutions</p>
    <p class="products">Pumping technology<span class="sep">|</span>Valve &amp; actuation<span class="sep">|</span>Air moving technology</p>
  </section>

</main>
</body>
</html>
```